Website for community Internet Radio station online 24/7

Home page with weather, clock, index, page headings and embedded radio player, and stop press block for moving banner with news.
Pages for schedule, blog, Presenters, new music/video and picture gallery and contact form.
Target Market(s)
Anybody anywhere. Internet around the eorld
Industry/Entity Type
Internet Radio station
Coding
Coded - Design and coding required
Number of Pages Required
5+ page
Font styles to use
Sans Serif
Requirements
Must have
- Embedded music player.

```html
<!DOCTYPE html>
<html lang="en">
<head>
<meta charset="utf-8">
<title>Wavelength Radio</title>
<link href="https://fonts.googleapis.com/css2?family=Poppins:ital,wght@0,400;0,500;0,600;0,700;0,800;1,500;1,700&display=swap" rel="stylesheet">
<style>
:root{
  --teal:#24889a;
  --green:#7cc636;
  --green-text:#78bf3c;
  --orange:#f7931e;
  --red:#e6252b;
  --purple:#7d3fa9;
  --ink:#222;
  --body:#444;
  --pale:#edf4f5;
  --card:#f4f4f4;
  --footer:#2b2b2b;
}
*{margin:0;padding:0;box-sizing:border-box}
html,body{width:1200px;height:4325px;overflow:hidden}
body{font-family:'Poppins',sans-serif;color:var(--body);background:#fff;position:relative}
.abs{position:absolute}
.btn{position:absolute;display:flex;align-items:center;justify-content:center;border-radius:30px;color:#fff;font-weight:600;text-transform:uppercase;font-size:17px}
.ph{position:absolute}

/* header */
.weather-icon{left:74px;top:28px}
.temp{left:154px;top:22px;font-size:36px;color:var(--ink);font-weight:500;line-height:1}
.cond{left:157px;top:68px;font-size:12px;color:var(--ink);font-weight:500}
.cond span{color:#888;font-weight:400;font-size:10px}
.clock{left:792px;top:46px;font-size:17px;color:#333;font-weight:500;display:flex;align-items:center;gap:10px}
.schedule{left:925px;top:32px;width:201px;height:50px;background:var(--green);font-size:16px}
.nav{left:0;top:117px;width:1200px;height:58px;background:var(--teal)}
.nav a{position:absolute;top:22px;color:#fff;font-size:14px;font-weight:600;text-decoration:none;text-transform:uppercase}
.logo-tab{left:500px;top:0;width:200px;height:160px;background:#fff;border-radius:0 0 100px 100px}
.brand{position:absolute;width:200px;text-align:center}
.brand .dot{width:34px;height:34px;border-radius:50%;background:var(--teal);margin:0 auto 10px}
.brand .name{font-size:14px;font-weight:700;color:var(--red);text-transform:uppercase;line-height:1.2}
.logo{left:500px;top:40px}

/* hero */
.hero{left:0;top:175px;width:1200px;height:636px;background:radial-gradient(circle at 70% 40%,#9aa4b0 0,#6b5a55 25%,#4a3430 45%,#c0703a 70%,#3b2a30 100%)}
.hero-box{left:74px;top:331px;width:423px;height:312px;background:rgba(40,40,40,.75);padding:24px 22px}
.hero-box .date{color:var(--green);font-size:16px;font-weight:600}
.hero-box h1{color:#fff;font-size:24px;font-weight:700;line-height:1.35;margin-top:6px}
.hero-box p{color:#eee;font-size:17px;line-height:1.7;margin-top:14px}
.hero-btn{left:97px;top:556px;width:178px;height:54px;background:var(--red)}
.ticker{left:74px;top:671px;color:#fff;font-size:14px;display:flex;gap:10px}
.player{left:705px;top:656px;width:421px;height:210px;border-radius:12px;background:linear-gradient(160deg,#3bb3a2 0%,#4a8fb8 45%,#8a3fb0 100%);padding:26px 23px;color:#fff}
.player h2{font-size:30px;font-weight:700;text-transform:uppercase;line-height:1.2}
.player .sub{font-size:14px;font-style:italic;margin-top:2px}
.player .song{font-size:18px;font-weight:600;margin-top:14px}
.audio{margin-top:10px;height:50px;background:#f1f3f4;border-radius:25px;display:flex;align-items:center;padding:0 18px;color:#222;font-size:16px;gap:14px}
.audio .bar{width:56px;height:4px;background:#999;border-radius:2px;position:relative}
.audio .bar i{position:absolute;left:0;top:0;width:36px;height:4px;background:#222}
.audio .bar b{position:absolute;left:30px;top:-5px;width:14px;height:14px;border-radius:50%;background:#222}

/* about */
.about-bg{left:0;top:923px;width:1200px;height:527px;background:var(--pale)}
.about-stripe{left:0;top:923px;width:1200px;height:527px;background:var(--teal);clip-path:polygon(537px 0,1200px 0,1200px 100%,674px 100%)}
.about-photo{left:0;top:923px;width:1200px;height:527px;background:linear-gradient(120deg,#5a4d40,#b98a55 40%,#3e5266 70%,#2c3440);clip-path:polygon(551px 0,1200px 0,1200px 100%,688px 100%)}
.sec-title{font-size:54px;font-weight:800;color:var(--ink);text-transform:uppercase;letter-spacing:1px;line-height:1.2}
.about-text{left:74px;top:990px;width:520px}
.about-text p{font-size:15px;line-height:30.5px;margin-top:16px}
.about-btn{left:74px;top:1313px;width:178px;height:54px;background:var(--orange)}

/* index */
.index-title{left:0;top:1506px;width:1200px;text-align:center}
.index-box{left:74px;top:1599px;width:1052px;height:390px;border:1px solid #ddd;border-radius:12px}
.idx{position:absolute;width:455px}
.idx .thumb{position:absolute;left:0;top:0;width:123px;height:104px;border-radius:10px;background:linear-gradient(135deg,#5a5048,#2c2623)}
.idx .txt{position:absolute;left:141px;top:0;width:325px}
.idx h3{font-size:18px;color:var(--green-text);font-weight:600;line-height:1.3}
.idx p{font-size:15px;line-height:24px;margin-top:2px}
.idx a{font-size:14px;color:var(--purple);font-weight:600;font-style:italic;text-decoration:underline}
.idx .rule{position:absolute;left:141px;top:114px;width:310px;height:1px;background:#ddd}

/* presenters */
.pres-bg{left:0;top:2061px;width:1200px;height:527px;background:var(--pale)}
.pres-stripe{left:0;top:2061px;width:1200px;height:527px;background:var(--teal);clip-path:polygon(0 0,600px 0,468px 100%,0 100%)}
.pres-photo{left:0;top:2061px;width:1200px;height:527px;background:linear-gradient(120deg,#8a2a2a,#3b4d6a 40%,#8a6a55 70%,#c99a80);clip-path:polygon(0 0,585px 0,455px 100%,0 100%)}
.pres-text{left:616px;top:2126px;width:520px}
.pres-text p{font-size:15px;line-height:30.5px;margin-top:16px}
.pres-btn{left:616px;top:2449px;width:178px;height:54px;background:var(--orange)}

/* gallery */
.gal-title{left:0;top:2630px;width:1200px;text-align:center}
.tabs{left:0;top:2731px;width:1200px;display:flex;justify-content:center;gap:22px;font-size:15px;color:#333;align-items:center}
.tabs .on{background:var(--teal);color:#fff;border-radius:20px;padding:6px 16px;font-weight:500}
.gcard{position:absolute;top:2807px;width:329px;height:183px;background:var(--card);border-radius:10px;padding:26px 21px}
.gcard h3{font-size:18px;color:var(--teal);font-weight:700;text-transform:uppercase}
.gcard p{font-size:15px;line-height:27px;margin-top:6px}
.gcard .meta{display:flex;align-items:center;gap:10px;margin-top:10px;font-size:15px;color:var(--red)}
.gcard .meta span{border:1px solid var(--purple);color:var(--purple);border-radius:16px;padding:3px 14px;font-size:13px;font-weight:600;text-transform:uppercase}

/* blog */
.blog-bg{left:0;top:3049px;width:1200px;height:614px;background:var(--pale)}
.blog-title{left:0;top:3103px;width:1200px;text-align:center}
.blog-main{left:74px;top:3205px;width:513px;height:386px;background:linear-gradient(135deg,#222 0,#3a3a3a 50%,#6b1a1a 80%,#1a1a1a)}
.blog-main .cap{position:absolute;left:25px;bottom:28px;width:420px;color:#fff}
.blog-main h3{color:var(--green);font-size:22px;font-weight:600}
.blog-main p{font-size:15px;line-height:24px;margin-top:4px}
.bside{position:absolute;left:616px;width:510px;height:175px}
.bside .thumb{position:absolute;left:0;top:0;width:238px;height:175px;background:linear-gradient(135deg,#6d625a,#c9c2b8)}
.bside .txt{position:absolute;left:257px;top:0;width:245px}
.bside h3{color:var(--green-text);font-size:22px;font-weight:600;line-height:1.35}
.bside p{font-size:15px;line-height:26px;margin-top:4px}
.bside a{font-size:14px;color:var(--purple);font-weight:600;font-style:italic;text-decoration:underline}

/* newsletter */
.news{left:74px;top:3712px;width:1052px;height:253px;border-radius:10px;background:linear-gradient(120deg,#3aaa9c 0%,#4fb8b3 50%,#6dcbd6 100%)}
.news-title{left:401px;top:3760px;color:#fff;font-size:30px;font-weight:700;text-transform:uppercase;white-space:nowrap;line-height:1.2}
.news-sub{left:401px;top:3806px;color:#fff;font-size:18px}
.news-form{left:403px;top:3851px;width:674px;height:59px;background:#fff;border-radius:30px;display:flex;align-items:center;padding-left:30px;font-size:15px;color:#333}
.news-btn{left:922px;top:3855px;width:150px;height:51px;background:var(--orange)}

/* footer */
.footer{left:0;top:4031px;width:1200px;height:294px;background:var(--footer)}
.foot-head{font-size:22px;font-style:italic;font-weight:700;color:#fff}
.fl{position:absolute;font-size:14px;line-height:41px}
.fl a{display:block;color:#ddd;text-decoration:none}
.flogo{left:500px;top:4090px}
.copy{left:0;top:4218px;width:1200px;text-align:center;font-size:14px;color:#ddd}
.social{left:0;top:4255px;width:1200px;display:flex;justify-content:center;gap:28px}
.social i{display:block;width:28px;height:28px;background:#fff;border-radius:4px}
.contact{left:861px;top:4117px;width:300px;font-size:14px;line-height:26px;color:#ddd}
</style>
</head>
<body>

<!-- header -->
<svg class="abs weather-icon" width="62" height="48" viewBox="0 0 62 48" aria-hidden="true">
  <circle cx="44" cy="14" r="9" fill="#f7b51e"/>
  <g stroke="#f7b51e" stroke-width="2"><line x1="44" y1="0" x2="44" y2="3"/><line x1="58" y1="14" x2="55" y2="14"/><line x1="54" y1="4" x2="52" y2="6"/><line x1="34" y1="4" x2="36" y2="6"/></g>
  <path d="M10 36a10 10 0 0 1 4-19 14 14 0 0 1 26 4 8 8 0 0 1 0 15z" fill="#fff" stroke="#2d5fa0" stroke-width="3"/>
  <path d="M18 40l-2 6M28 40l-2 6" stroke="#2d5fa0" stroke-width="3" stroke-linecap="round"/>
</svg>
<div class="abs temp">35°</div>
<div class="abs cond">Thundershower <span>| Lightly Polluted</span></div>
<div class="abs clock">
  <svg width="18" height="18" viewBox="0 0 18 18" aria-hidden="true"><circle cx="9" cy="9" r="7.5" fill="none" stroke="#7d3fa9" stroke-width="1.8"/><path d="M9 4.5V9l3 2" fill="none" stroke="#7d3fa9" stroke-width="1.8"/></svg>12:25:35
</div>
<div class="btn schedule">Schedule Now</div>

<nav class="abs nav">
  <a style="left:74px">Home</a>
  <a style="left:158px">About Us</a>
  <a style="left:274px">Radio</a>
  <a style="left:358px">Music</a>
  <a style="left:740px">Presenters</a>
  <a style="left:872px">Blog</a>
  <a style="left:948px">Gallery</a>
  <a style="left:1050px">Contact</a>
</nav>
<div class="abs logo-tab"></div>
<div class="brand logo">
  <div class="dot"></div>
  <div class="name">Wavelength Radio</div>
</div>

<!-- hero -->
<div class="ph hero" role="img" aria-label="Studio microphone in front of a softly blurred, colourful mixing desk"></div>
<div class="abs hero-box">
  <div class="date">DEC 21, 2022</div>
  <h1>Neque porro quisquam est qui dolorem ipsum quia dolor</h1>
  <p>Sed ut perspiciatis unde omnis iste natus error sit voluptatem accusantium doloremque laudantium.</p>
</div>
<div class="btn hero-btn">Read More</div>
<div class="abs ticker"><span>❚❚ Stop</span><span>▶ Play</span></div>

<div class="abs player">
  <h2>Music Player</h2>
  <div class="sub">Sed ut perspiciatis unde omnis iste natus.</div>
  <div class="song">Song Title Here</div>
  <div class="audio">
    <svg width="14" height="16" viewBox="0 0 14 16" aria-hidden="true"><rect x="1" y="1" width="4" height="14" fill="#222"/><rect x="9" y="1" width="4" height="14" fill="#222"/></svg>
    <span>54:29 / 1:36:59</span>
    <div class="bar"><i></i><b></b></div>
    <svg width="20" height="18" viewBox="0 0 20 18" style="margin-left:20px" aria-hidden="true"><path d="M1 6h4l5-4v14l-5-4H1z" fill="#222"/><path d="M13 5a5 5 0 0 1 0 8M15 2a9 9 0 0 1 0 14" fill="none" stroke="#222" stroke-width="1.8"/></svg>
    <svg width="4" height="16" viewBox="0 0 4 16" aria-hidden="true"><circle cx="2" cy="2" r="2" fill="#222"/><circle cx="2" cy="8" r="2" fill="#222"/><circle cx="2" cy="14" r="2" fill="#222"/></svg>
  </div>
</div>

<!-- about -->
<div class="abs about-bg"></div>
<div class="abs about-stripe"></div>
<div class="ph about-photo" role="img" aria-label="Two smiling hosts in headphones recording at studio microphones"></div>
<div class="abs about-text">
  <h2 class="sec-title">About Us</h2>
  <p>Sed ut perspiciatis unde omnis iste natus error sit voluptatem accusantium doloremque laudantium, totam rem aperiam, eaque ipsa quae ab illo inventore veritatis et quasi architecto beatae vitae dicta sunt explicabo. Nemo enim ipsam voluptatem quia voluptas sit aspernatur aut odit aut fugit, sed quia consequuntur magni dolores eos qui ratione voluptatem quis nostrum exercitationem ullam corporis.</p>
</div>
<div class="btn about-btn">Read More</div>

<!-- index -->
<div class="abs index-title"><h2 class="sec-title">Index</h2></div>
<div class="abs index-box"></div>

<div class="idx" style="left:97px;top:1616px"><div class="thumb" role="img" aria-label="Radio studio with presenters"></div><div class="txt"><h3>Sed ut perspiciatis unde omnis</h3><p>Nemo enim ipsam voluptatem quia volu aspernatur aut odit aut fugit.</p><a>More Info</a></div><div class="rule"></div></div>
<div class="idx" style="left:617px;top:1616px"><div class="thumb" role="img" aria-label="Two hosts at a podcast desk" style="background:linear-gradient(135deg,#d8d2c8,#8a7a6a)"></div><div class="txt"><h3>Sed ut perspiciatis unde omnis</h3><p>Nemo enim ipsam voluptatem quia volu aspernatur aut odit aut fugit.</p><a>More Info</a></div><div class="rule"></div></div>
<div class="idx" style="left:97px;top:1740px"><div class="thumb" role="img" aria-label="Presenter speaking into a microphone at a laptop" style="background:linear-gradient(135deg,#c9c6c2,#5a4a42)"></div><div class="txt"><h3>Sed ut perspiciatis unde omnis</h3><p>Nemo enim ipsam voluptatem quia volu aspernatur aut odit aut fugit.</p><a>More Info</a></div><div class="rule"></div></div>
<div class="idx" style="left:617px;top:1740px"><div class="thumb" role="img" aria-label="Group of hosts around a studio table" style="background:linear-gradient(135deg,#7aa0c0,#5a4a3a)"></div><div class="txt"><h3>Sed ut perspiciatis unde omnis</h3><p>Nemo enim ipsam voluptatem quia volu aspernatur aut odit aut fugit.</p><a>More Info</a></div><div class="rule"></div></div>
<div class="idx" style="left:97px;top:1864px"><div class="thumb" role="img" aria-label="Team in a dark studio with a bright screen" style="background:linear-gradient(135deg,#2a2a30,#8090a0)"></div><div class="txt"><h3>Sed ut perspiciatis unde omnis</h3><p>Nemo enim ipsam voluptatem quia volu aspernatur aut odit aut fugit.</p><a>More Info</a></div></div>
<div class="idx" style="left:617px;top:1864px"><div class="thumb" role="img" aria-label="Host in headphones at a studio microphone" style="background:linear-gradient(135deg,#4a4440,#c09070)"></div><div class="txt"><h3>Sed ut perspiciatis unde omnis</h3><p>Nemo enim ipsam voluptatem quia volu aspernatur aut odit aut fugit.</p><a>More Info</a></div></div>

<!-- presenters -->
<div class="abs pres-bg"></div>
<div class="abs pres-stripe"></div>
<div class="ph pres-photo" role="img" aria-label="Presenter in a knit hat holding a microphone beside a broadcast screen"></div>
<div class="abs pres-text">
  <h2 class="sec-title">Presenters</h2>
  <p>Sed ut perspiciatis unde omnis iste natus error sit voluptatem accusantium doloremque laudantium, totam rem aperiam, eaque ipsa quae ab illo inventore veritatis et quasi architecto beatae vitae dicta sunt explicabo. Nemo enim ipsam voluptatem quia voluptas sit aspernatur aut odit aut fugit, sed quia consequuntur magni dolores eos qui ratione voluptatem quis nostrum exercitationem ullam corporis.</p>
</div>
<div class="btn pres-btn">Read More</div>

<!-- gallery -->
<div class="abs gal-title"><h2 class="sec-title">Gallery</h2></div>
<div class="abs tabs"><span>ALL</span><span class="on">NEW MUSIC</span><span>VIDEO</span><span>PHOTO</span></div>
<svg class="abs" style="left:40px;top:2880px" width="20" height="36" viewBox="0 0 20 36" aria-hidden="true"><path d="M17 2L3 18l14 16" fill="none" stroke="#555" stroke-width="2.5"/></svg>
<svg class="abs" style="left:1140px;top:2880px" width="20" height="36" viewBox="0 0 20 36" aria-hidden="true"><path d="M3 2l14 16L3 34" fill="none" stroke="#555" stroke-width="2.5"/></svg>
<div class="gcard" style="left:74px"><h3>Music Heading</h3><p>Sed ut perspiciatis unde omnis iste natus error sit voluptatem.</p><div class="meta">5:02 mins <span>Play Music</span></div></div>
<div class="gcard" style="left:436px"><h3>Music Heading</h3><p>Sed ut perspiciatis unde omnis iste natus error sit voluptatem.</p><div class="meta">5:02 mins <span>Play Music</span></div></div>
<div class="gcard" style="left:797px"><h3>Music Heading</h3><p>Sed ut perspiciatis unde omnis iste natus error sit voluptatem.</p><div class="meta">5:02 mins <span>Play Music</span></div></div>

<!-- blog -->
<div class="abs blog-bg"></div>
<div class="abs blog-title"><h2 class="sec-title">Blog</h2></div>
<div class="abs blog-main">
  <div class="ph" style="inset:0" role="img" aria-label="Studio microphone in front of a glowing on-air sign"></div>
  <div class="cap"><h3>Sed ut perspiciatis unde omnis</h3><p>Nemo enim ipsam voluptatem quia volu aspernatur aut odit aut fugit.</p></div>
</div>
<div class="bside" style="top:3205px"><div class="thumb" role="img" aria-label="Two hosts recording at microphones with laptops"></div><div class="txt"><h3>Sed ut perspiciatis unde omnis</h3><p>Nemo enim ipsam voluptatem quia volu aspernatur aut odit aut fugit.</p><a>More Info</a></div></div>
<div class="bside" style="top:3416px"><div class="thumb" role="img" aria-label="Laughing hosts in headphones during a broadcast" style="background:linear-gradient(135deg,#8a8580,#e0c060 60%,#6a5a50)"></div><div class="txt"><h3>Sed ut perspiciatis unde omnis</h3><p>Nemo enim ipsam voluptatem quia volu aspernatur aut odit aut fugit.</p><a>More Info</a></div></div>

<!-- newsletter -->
<div class="abs news"></div>
<h2 class="abs news-title">Newsletter Subscribe</h2>
<div class="abs news-sub">Nemo enim ipsam voluptatem quia voluptas sit aspernatur aut odit.</div>
<div class="abs news-form">Enter Email Address</div>
<div class="btn news-btn">Sign Up</div>

<!-- footer -->
<footer class="abs footer"></footer>
<h4 class="abs foot-head" style="left:75px;top:4075px">Quick Links</h4>
<div class="fl" style="left:75px;top:4110px"><a>Home</a><a>About Us</a><a>Radio</a><a>Music</a></div>
<div class="fl" style="left:253px;top:4110px"><a>Presenters</a><a>Blog</a><a>Gallery</a><a>Contact</a></div>
<div class="brand flogo">
  <div class="dot"></div>
  <div class="name">Wavelength Radio</div>
</div>
<div class="abs copy">©2022 by Wavelength Radio. All Right Reserved</div>
<div class="abs social"><i></i><i></i><i></i><i></i></div>
<h4 class="abs foot-head" style="left:861px;top:4075px">Contact Info</h4>
<div class="abs contact">
  12 Harbour Lane, Northfield, NF4 2QT,<br>United Kingdom
  <div style="margin-top:12px">1-800-555-0147</div>
  <div style="margin-top:12px">info@wavelengthradio.example</div>
</div>

</body>
</html>
```